Travel agency website refresh

I want to refresh and simplify my current Wordpress.com website. Same general color scheme but modernize and make it user friendly for all devices. Must work with Wordpress. No live booking engines. We are a boutique luxury travel agency. Think luxury, vacation, boho chic, elegant, lush, tropical, cruises, first class. Romance and adventure.
Updates

Target Market(s)

Luxury travelers

Industry/Entity Type

Travel

Coding

Coded - Design and coding required

Number of Pages Required

5+ page

Font styles to use
Sans Serif

Colors
0094D4
00A9DD
6FCCEA
C7EBF8
E9F6FB

Requirements
Must have
• Compatible with Wordpress.com, homepage, about page, contact page, faq page
Nice to have
• The homepage should quickly tell the consumer the type of travel I specialize in. My current website has this (journeyswithmaren.example). I’d like to incorporate the about me as a preview on the home page.
Should not have
• Harsh colors, look generic

```html
<!DOCTYPE html>
<html lang="en">
<head>
<meta charset="utf-8">
<title>FAQs | Journeys with Maren</title>
<link href="https://fonts.googleapis.com/css2?family=Oswald:wght@400;500&family=Outfit:wght@300;400&family=Allura&display=swap" rel="stylesheet">
<style>
:root{
  --ink:#232323;
  --body:#4a4a4a;
  --teal:#5cc3c8;
  --teal-soft:#c7ebf8;
  --brand:#857564;
  --line:#cfcfcf;
  --chev-bg:#dcd7d1;
  --white:#ffffff;
  --black:#1d1d1d;
}
*{box-sizing:border-box;margin:0;padding:0}
html,body{width:1200px;height:3152px;overflow:hidden;background:var(--white)}
body{position:relative;font-family:'Outfit',sans-serif;color:var(--ink)}
.brand{display:flex;align-items:center;gap:10px}
.brand-dot{width:44px;height:44px;border-radius:50%;background:var(--teal);flex:none}
.brand-name{font-family:'Oswald',sans-serif;font-weight:400;color:var(--brand);line-height:1.05;text-transform:uppercase;white-space:nowrap}
.site-header{position:absolute;top:0;left:0;width:1200px;height:113px}
.site-header .brand{position:absolute;left:111px;top:26px}
.site-header .brand-name{font-size:20px}
.nav{position:absolute;left:377px;top:44px;display:flex;gap:28px;font-family:'Oswald',sans-serif;font-size:17px;color:#3a3a3a}
.nav .active{color:var(--teal)}
.contact-btn{position:absolute;left:964px;top:31px;width:124px;height:53px;border:1.5px solid #333;display:flex;align-items:center;justify-content:center;font-family:'Outfit',sans-serif;font-size:19px;font-weight:400;letter-spacing:.3px}
.hero{position:absolute;top:113px;left:0;width:1200px;height:344px;background:linear-gradient(180deg,#b9a58c 0%,#d7c2a3 40%,#8fa7ad 62%,#e4d6c2 80%,#cbb79d 100%)}
.hero h1{position:absolute;left:109px;top:94px;font-family:'Oswald',sans-serif;font-weight:500;font-size:54px;line-height:84px;color:var(--white);text-transform:uppercase}
.faq-intro{position:absolute;top:520px;left:0;width:1200px;text-align:center}
.script{font-family:'Allura',cursive;color:#6f5f50}
.faq-intro .script{font-size:44px}
.faq-intro h2{font-family:'Oswald',sans-serif;font-weight:500;font-size:36px;margin-top:14px;text-transform:uppercase}
.faq{position:absolute;top:685px;left:210px;width:780px}
.faq-item{border-bottom:1.5px solid var(--line)}
.faq-q{display:flex;align-items:center;justify-content:space-between;padding:18px 24px 18px 20px;min-height:68px;font-size:20px;line-height:26px}
.chev{width:36px;height:36px;border-radius:50%;background:var(--chev-bg);flex:none;display:flex;align-items:center;justify-content:center}
.chev.open{background:var(--teal)}
.faq-a{padding:8px 20px 18px 30px;font-size:15.5px;line-height:25.7px;color:var(--body);font-weight:300}
.faq-item.open{border-bottom:none}
.faq-item.open .faq-q{border-bottom:1.5px solid var(--line)}
.signup{position:absolute;top:2171px;left:0;width:1200px;height:520px;background:linear-gradient(180deg,#fbe3c6 0%,#f3dfca 30%,#b9c3c7 55%,#8ea5b3 75%,#a7b4bc 100%)}
.signup .script{position:absolute;left:110px;top:80px;font-size:46px}
.signup h2{position:absolute;left:112px;top:146px;font-family:'Oswald',sans-serif;font-weight:500;font-size:36px;line-height:71px;text-transform:uppercase;color:var(--ink)}
.signup-form{position:absolute;left:111px;top:315px;display:flex}
.signup-input{width:437px;height:67px;background:var(--white);padding-left:20px;display:flex;align-items:center;font-size:17px;color:#333}
.signup-btn{width:72px;height:67px;background:var(--black);display:flex;align-items:center;justify-content:center}
.site-footer{position:absolute;top:2691px;left:0;width:1200px;height:461px}
.site-footer .brand{position:absolute;left:109px;top:60px}
.site-footer .brand-dot{width:90px;height:90px}
.site-footer .brand-name{font-size:28px}
.footer-contact{position:absolute;left:110px;top:242px;font-size:16px;line-height:32px;color:var(--ink)}
.footer-contact div{display:flex;align-items:center;gap:6px}
.badge{position:absolute;background:#e3e3e3;border-radius:4px}
.badge.one{left:388px;top:135px;width:183px;height:32px}
.badge.two{left:388px;top:196px;width:140px;height:51px;border-radius:26px}
.footer-links{position:absolute;top:64px;font-size:16px;line-height:26.7px;list-style:none;color:#333}
.footer-links.a{left:621px}
.footer-links.b{left:926px}
.footer-rule{position:absolute;top:357px;left:110px;width:969px;border-top:1.5px solid #cfcfcf}
.copyright{position:absolute;top:391px;left:110px;font-size:16px}
.socials{position:absolute;top:379px;left:937px;display:flex;gap:8px}
.socials span{width:44px;height:44px;border:1.5px solid var(--teal);border-radius:50%}
</style>
</head>
<body>
<header class="site-header">
  <div class="brand"><span class="brand-dot"></span><span class="brand-name">Journeys<br>with Maren</span></div>
  <nav class="nav">
    <span>Home</span><span>About</span><span>Why Book With Us?</span><span>Blog</span><span class="active">FAQs</span><span>Forms &amp; Questionnaires</span>
  </nav>
  <div class="contact-btn">CONTACT</div>
</header>

<section class="hero" role="img" aria-label="Family walking hand in hand on a tropical beach at sunset near overwater bungalows">
  <h1>Frequently Asked<br>Questions</h1>
</section>

<section class="faq-intro">
  <div class="script">Question &amp; Answers</div>
  <h2>Frequently Asked Questions</h2>
</section>

<section class="faq">
  <div class="faq-item open">
    <div class="faq-q">What is Journeys with Maren?<span class="chev open"><svg width="14" height="9" viewBox="0 0 14 9"><path d="M1 8l6-6 6 6" fill="none" stroke="#fff" stroke-width="1.8"/></svg></span></div>
    <div class="faq-a">Journeys with Maren is a boutique travel agency headquartered in Alder Falls, New Hampshire owned and operated by Maren Ellis. Maren is a professional travel agent with over 27 years experience. She specializes in romance travel (honeymoons, babymoons, anniversary trips, small destination weddings etc), family vacations, luxury cruises &amp; tours and customized vacation planning to exciting destinations around the globe. Other than cruises that originate from the US, Hawaii and Alaska, she specializes in International destinations. &nbsp; Learn more about how she got her start in this biz back in 1996!</div>
  </div>
  <div class="faq-item"><div class="faq-q">Where is your office located?<span class="chev"><svg width="14" height="9" viewBox="0 0 14 9"><path d="M1 1l6 6 6-6" fill="none" stroke="#fff" stroke-width="1.8"/></svg></span></div></div>
  <div class="faq-item"><div class="faq-q">Doesn’t it cost more to book with a travel agent?<span class="chev"><svg width="14" height="9" viewBox="0 0 14 9"><path d="M1 1l6 6 6-6" fill="none" stroke="#fff" stroke-width="1.8"/></svg></span></div></div>
  <div class="faq-item"><div class="faq-q">Do you charge service fees?<span class="chev"><svg width="14" height="9" viewBox="0 0 14 9"><path d="M1 1l6 6 6-6" fill="none" stroke="#fff" stroke-width="1.8"/></svg></span></div></div>
  <div class="faq-item"><div class="faq-q"><span>I’ve never worked with a travel agent before.<br>What do i need to know? How are you paid?</span><span class="chev"><svg width="14" height="9" viewBox="0 0 14 9"><path d="M1 1l6 6 6-6" fill="none" stroke="#fff" stroke-width="1.8"/></svg></span></div></div>
  <div class="faq-item"><div class="faq-q">Is there anything you don’t book?<span class="chev"><svg width="14" height="9" viewBox="0 0 14 9"><path d="M1 1l6 6 6-6" fill="none" stroke="#fff" stroke-width="1.8"/></svg></span></div></div>
  <div class="faq-item"><div class="faq-q"><span>I have a ton of frequent flyer miles, hotel points, credit card points etc.<br>Can you book my trip?</span><span class="chev"><svg width="14" height="9" viewBox="0 0 14 9"><path d="M1 1l6 6 6-6" fill="none" stroke="#fff" stroke-width="1.8"/></svg></span></div></div>
  <div class="faq-item"><div class="faq-q">How do we know you’re a real business?<span class="chev"><svg width="14" height="9" viewBox="0 0 14 9"><path d="M1 1l6 6 6-6" fill="none" stroke="#fff" stroke-width="1.8"/></svg></span></div></div>
  <div class="faq-item"><div class="faq-q">What is the best way to pick a travel agent?<span class="chev"><svg width="14" height="9" viewBox="0 0 14 9"><path d="M1 1l6 6 6-6" fill="none" stroke="#fff" stroke-width="1.8"/></svg></span></div></div>
  <div class="faq-item"><div class="faq-q">How far in advance should i book my trip?<span class="chev"><svg width="14" height="9" viewBox="0 0 14 9"><path d="M1 1l6 6 6-6" fill="none" stroke="#fff" stroke-width="1.8"/></svg></span></div></div>
  <div class="faq-item"><div class="faq-q">Do you offer payment plans?<span class="chev"><svg width="14" height="9" viewBox="0 0 14 9"><path d="M1 1l6 6 6-6" fill="none" stroke="#fff" stroke-width="1.8"/></svg></span></div></div>
  <div class="faq-item"><div class="faq-q">Do i need a passport?<span class="chev"><svg width="14" height="9" viewBox="0 0 14 9"><path d="M1 1l6 6 6-6" fill="none" stroke="#fff" stroke-width="1.8"/></svg></span></div></div>
  <div class="faq-item"><div class="faq-q">What about covid-19?<span class="chev"><svg width="14" height="9" viewBox="0 0 14 9"><path d="M1 1l6 6 6-6" fill="none" stroke="#fff" stroke-width="1.8"/></svg></span></div></div>
  <div class="faq-item"><div class="faq-q">What about the zika virus?<span class="chev"><svg width="14" height="9" viewBox="0 0 14 9"><path d="M1 1l6 6 6-6" fill="none" stroke="#fff" stroke-width="1.8"/></svg></span></div></div>
  <div class="faq-item"><div class="faq-q">Should i just book direct with the resort or cruise line?<span class="chev"><svg width="14" height="9" viewBox="0 0 14 9"><path d="M1 1l6 6 6-6" fill="none" stroke="#fff" stroke-width="1.8"/></svg></span></div></div>
  <div class="faq-item"><div class="faq-q"><span>How do you compare with dealbunch, staylist.example,<br>tripmarket and similar discount sites?</span><span class="chev"><svg width="14" height="9" viewBox="0 0 14 9"><path d="M1 1l6 6 6-6" fill="none" stroke="#fff" stroke-width="1.8"/></svg></span></div></div>
</section>

<section class="signup" role="img" aria-label="Woman relaxing in an infinity pool overlooking the sea and a cruise ship at sunset">
  <div class="script">Get inspired for your next gateway.</div>
  <h2>Sign up to receive travel tips<br>and inspiration</h2>
  <div class="signup-form">
    <div class="signup-input">Email Address</div>
    <div class="signup-btn"><svg width="24" height="22" viewBox="0 0 24 22"><path d="M23 1L1 10l7 3 2 8 4-6 6 3z" fill="#fff"/></svg></div>
  </div>
</section>

<footer class="site-footer">
  <div class="brand"><span class="brand-dot"></span><span class="brand-name">Journeys<br>with Maren</span></div>
  <div class="footer-contact">
    <div><svg width="13" height="13" viewBox="0 0 24 24"><path d="M6.6 10.8a15 15 0 006.6 6.6l2.2-2.2c.3-.3.7-.4 1-.2 1.1.4 2.3.6 3.6.6.6 0 1 .4 1 1V20c0 .6-.4 1-1 1C10.6 21 3 13.4 3 4c0-.6.4-1 1-1h3.5c.6 0 1 .4 1 1 0 1.3.2 2.5.6 3.6.1.3 0 .7-.2 1z" fill="#5cc3c8"/></svg>Tel: 555-014-2270</div>
    <div><svg width="14" height="11" viewBox="0 0 14 11"><rect width="14" height="11" rx="1" fill="#5cc3c8"/><path d="M0.5 1l6.5 5 6.5-5" fill="none" stroke="#fff" stroke-width="1.2"/></svg>Email: info@journeyswithmaren.example</div>
  </div>
  <div class="badge one" aria-label="Partner badge"></div>
  <div class="badge two" aria-label="Partner badge"></div>
  <ul class="footer-links a">
    <li>Frequently Asked Questions</li><li>Posts about Custom Trips</li><li>Posts about Honeymoons &amp; Romance</li><li>Posts about Family Travel</li><li>Posts about Cruise Vacations</li><li>Posts about Travel Tips</li><li>Welcome Home</li><li>Booking Fee</li><li>Plan To Go Service Agreement</li><li>Cancellation Fee</li>
  </ul>
  <ul class="footer-links b">
    <li>Airline Ticket Fee</li><li>Concierge Services</li><li>Payment Form</li><li>Transfer Your Cruise Booking</li><li>Archives</li><li>Press Releases</li><li>JWM In the Press</li><li>Travel Tips</li><li>Travel Guides</li>
  </ul>
  <div class="footer-rule"></div>
  <div class="copyright">Copyright © 2024 · Journeys with Maren LLC. All rights reserved.</div>
  <div class="socials"><span aria-label="Social link"></span><span aria-label="Social link"></span><span aria-label="Social link"></span></div>
</footer>
</body>
</html>
```